Business card design Needed for new logo / Construction business, home extensions and new builds

We need a business card design using our new logo files which i will attach to this project :)

We are a small construction business specialising in home extensions, new builds and property development. We are very ambitious and would appreciate professional and elegant designs for our new business card.

Very serious about using the services on BriefNest and recently acquired our new logo from here :)

Please get involved, i will feedback when i can as i am very busy but can respond daily, thanks

Target Market(s)

People that want to build onto their houses, new building developments or adding too their existing property

Industry/Entity Type

Construction

Contact Information for Business Card

Hollin Marsh Construction, Tobias Renwick (Managing Director), Tel 07822200444, email - info@hollin-marsh, www.hollin-marsh.co.uk

Colors

Designer to choose colors to be used in the design.

Requirements
Must have
• I like a deep grey on the back please. A lot of you have provided black from and back, try mixing things up a little. The black looks cool 😎 Thanks

```html
<!DOCTYPE html>
<html lang="en">
<head>
<meta charset="utf-8">
<title>Hollin Marsh Construction – Business Card</title>
<link rel="stylesheet" href="https://fonts.googleapis.com/css2?family=Open+Sans:wght@400;600;700&display=swap">
<style>
  :root {
    --backdrop: #3b3b3b;
    --card-black: #141414;
    --card-deep: #1c1c1c;
    --gold: #d9a227;
    --gold-light: #f0c04a;
    --silver: #d6d6d6;
    --text-light: #e8e8e8;
  }
  * { margin: 0; padding: 0; box-sizing: border-box; }
  html, body {
    width: 1200px; height: 801px; overflow: hidden;
    background: var(--backdrop);
    font-family: "Open Sans", Arial, sans-serif;
  }
  .stage {
    position: relative; width: 1200px; height: 801px;
    display: flex; align-items: center; justify-content: center; gap: 40px;
  }
  .card {
    position: relative; width: 540px; height: 309px;
    border: 2px solid var(--gold);
    border-radius: 3px;
    box-shadow: 0 18px 40px rgba(0,0,0,0.45);
    overflow: hidden;
  }
  .card--front { background: var(--card-black); }
  .card--back { background: var(--card-deep); }

  .brand {
    position: absolute; left: 34px; top: 118px; width: 200px;
    display: flex; align-items: center; gap: 10px;
  }
  .brand__mark {
    flex: none; width: 26px; height: 26px; background: var(--gold);
  }
  .brand__name {
    color: var(--gold); font-weight: 600; font-size: 15px;
    line-height: 1.25; letter-spacing: 0.06em; text-transform: uppercase;
  }

  .divider {
    position: absolute; left: 262px; top: 70px;
    width: 1px; height: 170px; background: var(--gold);
  }

  .contact { position: absolute; left: 290px; top: 78px; }
  .contact__name {
    color: var(--gold); font-weight: 700; font-size: 20px;
    letter-spacing: 0.02em; text-transform: uppercase;
  }
  .contact__role { color: var(--text-light); font-size: 13px; margin-top: 2px; }
  .contact__list { list-style: none; margin-top: 22px; }
  .contact__item {
    display: flex; align-items: center; gap: 9px;
    color: var(--text-light); font-size: 13px; line-height: 24px;
  }
  .contact__icon { width: 12px; height: 12px; flex: none; }

  .pattern {
    position: absolute; inset: 0;
    background:
      radial-gradient(ellipse at 75% 30%, rgba(90,90,90,0.35), transparent 60%),
      linear-gradient(135deg, #101010 0%, #1f1f1f 55%, #2c2c2c 100%);
  }
  .back-brand {
    position: absolute; left: 50%; top: 50%; transform: translate(-50%, -50%);
    display: flex; align-items: center; gap: 10px;
  }
</style>
</head>
<body>
<main class="stage">
  <section class="card card--front" aria-label="Business card front">
    <div class="brand">
      <span class="brand__mark"></span>
      <span class="brand__name">Hollin Marsh Construction</span>
    </div>
    <div class="divider"></div>
    <div class="contact">
      <p class="contact__name">Tobias Renwick</p>
      <p class="contact__role">Managing Director</p>
      <ul class="contact__list">
        <li class="contact__item">
          <svg class="contact__icon" viewBox="0 0 12 12"><path fill="var(--gold)" d="M2.5 0.5l2 2-1 1.3c.6 1.4 1.6 2.4 3 3L7.8 5.8l2 2-1.3 1.7C4.5 9.5.8 5.6 1 1.7z"/></svg>
          07822200444
        </li>
        <li class="contact__item">
          <svg class="contact__icon" viewBox="0 0 12 12"><rect x="0.5" y="2.5" width="11" height="7" fill="var(--gold)"/><path d="M0.5 2.5L6 6.5l5.5-4" fill="none" stroke="var(--card-black)" stroke-width="1"/></svg>
          info@hollin-marsh
        </li>
        <li class="contact__item">
          <svg class="contact__icon" viewBox="0 0 12 12"><circle cx="6" cy="6" r="5.5" fill="var(--gold)"/><path d="M0.5 6h11M6 0.5c-2.5 3-2.5 8 0 11M6 0.5c2.5 3 2.5 8 0 11" fill="none" stroke="var(--card-black)" stroke-width="0.8"/></svg>
          www.hollin-marsh.co.uk
        </li>
      </ul>
    </div>
  </section>

  <section class="card card--back" aria-label="Business card back">
    <div class="pattern" role="img" aria-label="Repeating embossed brand pattern in black gloss tones"></div>
    <div class="back-brand">
      <span class="brand__mark"></span>
      <span class="brand__name">Hollin Marsh Construction</span>
    </div>
  </section>
</main>
</body>
</html>
```